Dentistry

Dentist's personal business card. No logo needed. The card shoul deliver the massage of reliability, professionalism, experience.
Please ad the full brief of the project: down the line it says: the winning look should be precise and pristine NO pictures of Teeth, smiles, instruments etc.

The details to be desplaid are:
Dr. Rob Valdoni
Doctor of Dental Surgery
PHD
Web. Www.drvaldoni.com
Email. Rob@drvaldoni.com
Tel 07731482590
Surgery address. 27Bharwick road London SW4 7QN UK
82 Fenwyn Row London SW3 2HT. Uk

Reason: Decided to make the payment unrefundable in order to get more designers involved.

Requirements
Should not have
• Logo, teeth, smile any sort of instruments.

```html
<!DOCTYPE html>
<html lang="en">
<head>
<meta charset="utf-8">
<title>Dr. Rob Valdoni – Business Card</title>
<link rel="stylesheet" href="https://fonts.googleapis.com/css2?family=Marcellus&family=Libre+Baskerville&display=swap">
<style>
  :root {
    --backdrop: #ececec;
    --card: #ffffff;
    --ink: #111111;
    --card-edge: #dddddd;
  }
  * { margin: 0; padding: 0; box-sizing: border-box; }
  html, body {
    width: 1200px;
    height: 1200px;
    overflow: hidden;
    background: var(--backdrop);
  }
  .canvas {
    position: relative;
    width: 1200px;
    height: 1200px;
  }
  .card {
    position: absolute;
    width: 716px;
    height: 412px;
    background: var(--card);
    border: 1px solid var(--card-edge);
    color: var(--ink);
  }
  .card--front { left: 252px; top: 94px; }
  .card--back  { left: 249px; top: 689px; }

  .card__name {
    position: absolute;
    left: 54px;
    top: 140px;
    font-family: "Marcellus", serif;
    font-weight: 400;
    font-size: 54px;
    letter-spacing: 3px;
    line-height: 1;
    text-transform: uppercase;
    white-space: nowrap;
  }
  .card__title {
    position: absolute;
    left: 55px;
    top: 206px;
    font-family: "Marcellus", serif;
    font-weight: 400;
    font-size: 28px;
    letter-spacing: 1px;
    line-height: 1;
    white-space: nowrap;
  }

  .contact {
    position: absolute;
    left: 0;
    right: 0;
    top: 106px;
    list-style: none;
    text-align: center;
    font-family: "Libre Baskerville", serif;
    font-size: 20px;
    line-height: 1;
  }
  .contact__item { height: 20px; white-space: nowrap; }
  .contact__item + .contact__item { margin-top: 21px; }
  .contact__item--web { margin-top: 24px !important; }
  .contact__item--address { margin-top: 18px !important; }
</style>
</head>
<body>
  <main class="canvas">
    <section class="card card--front" aria-label="Business card front">
      <h1 class="card__name">Dr. Rob Valdoni</h1>
      <p class="card__title">Doctor of Dental Surgery, PhD</p>
    </section>

    <section class="card card--back" aria-label="Business card back">
      <ul class="contact">
        <li class="contact__item">Tel: 07731482590</li>
        <li class="contact__item">Email: Rob@drvaldoni.com</li>
        <li class="contact__item contact__item--web">Www.drvaldoni.com</li>
        <li class="contact__item contact__item--address">27Bharwick road London SW4 7QN UK</li>
        <li class="contact__item contact__item--address">82 Fenwyn Row London SW3 2HT. Uk</li>
      </ul>
    </section>
  </main>
</body>
</html>
```